BRVL Brochure Design

Northfield Council of Clinical Standards (BRVL) needs a whole new brochure. I've upload EPS logos and past brochures. Our tagline is to "modernize healthcare" and we think our brochure should reflect that, so that's the purpose of this project.

BRVL is a proven leader in healthcare education, training and
consulting services for health professionals. We’ve earned a reputation for excellence in healthcare quality improvement and management.

BRVL works to improve healthcare quality by educating healthcare professionals about healthcare best practices. We focus on instructing our clients on how to plan for, measure, and improve healthcare quality in all facilities and facets such as:

Patient Safety
Infection Control
Performance Improvement
Risk Management
Compliance and Accreditation
Health and Hospital Administration
Health Insurance
Healthcare Financial Management
Facility Management and Safety

DESIGN SUGGESTIONS:

Brochure Size: 8.5 X 11 full size brochure or 8.5 X 11 trifold brochure

Number of Pages: 2 to 3

Colors: Feel free to use a wide array of colors but try to stay away from colors that are too loud, ex: Pink, Purple, Neon Green.

Themes: Professional, Educational

Designs:

Pelor by Oskar Lindqvist

Quorvo Pamphlet by Derek Malloway

Lanterns for harvest by Solvendri

Paisaje de Sr KT by vrpl

http://www.plimbask.com/post/28461937205/10-creative-brochure-designs

Don't limit yourself to these examples. However, these are examples we liked

Reason: We would like to see more designs

We want more full page designs than tri-fold 

We are considering both tri-fold and full-page but would like to see more full page designs 

Reason: Our lead designer making the decisions on this project has been fired. I apologize for the inconvenience. We want extend the project one last time

Target Market(s)

Students, Doctors, and Educational Professionals

Industry/Entity Type

Healthcare

Logo Text

asdfasdf

Font styles to use
Serif
Sans Serif
Decorative
Script

Requirements
Should not have
• Pink, Purple, Neon Green colors

```html
<!DOCTYPE html>
<html lang="en">
<head>
<meta charset="utf-8">
<title>BRVL Brochure</title>
<link rel="stylesheet" href="https://fonts.googleapis.com/css2?family=Mulish:ital,wght@0,400;0,700;1,400&family=Open+Sans:wght@300;700&display=swap">
<style>
:root{
  --navy:#0d1b6e;
  --blue:#1f6fd1;
  --band:#2f74c8;
  --band-dark:#1d5cb0;
  --ink:#2b2b2b;
  --sky:#c8d9f2;
  --white:#ffffff;
}
*{margin:0;padding:0;box-sizing:border-box}
html,body{width:1200px;height:927px;overflow:hidden;background:var(--white)}
body{position:relative;font-family:"Mulish",sans-serif;color:var(--ink)}
.abs{position:absolute}

.hero-strip{left:0;top:0;width:797px;height:166px;
  background:
    radial-gradient(ellipse 90px 110px at 150px 60px,#e3c2a6 0%,rgba(227,194,166,0) 70%),
    radial-gradient(ellipse 110px 120px at 380px 55px,#a9785c 0%,rgba(169,120,92,0) 70%),
    radial-gradient(ellipse 90px 160px at 380px 150px,#f4f6fa 0%,rgba(244,246,250,0) 70%),
    radial-gradient(ellipse 60px 80px at 540px 80px,#e2c6b2 0%,rgba(226,198,178,0) 70%),
    radial-gradient(ellipse 45px 60px at 620px 90px,#eddccf 0%,rgba(237,220,207,0) 70%),
    linear-gradient(90deg,#c3d4ee 0%,#e8dcd3 20%,#f3ebe4 50%,#eef1f6 80%,#ffffff 100%)}
.sweep{left:700px;top:0;width:110px;height:203px;border-bottom-right-radius:100% 100%;
  background:linear-gradient(180deg,rgba(200,217,242,0) 0%,var(--sky) 100%)}
.side-photo{left:797px;top:203px;width:403px;height:724px;
  border-top-left-radius:130px 240px;border-bottom-right-radius:60px 300px;
  background:
    radial-gradient(ellipse 150px 200px at 270px 200px,#f0cdb0 0%,rgba(240,205,176,0) 75%),
    radial-gradient(ellipse 150px 110px at 280px 60px,#c69a6a 0%,rgba(198,154,106,0) 75%),
    radial-gradient(ellipse 90px 160px at 80px 230px,#dbb89c 0%,rgba(219,184,156,0) 75%),
    radial-gradient(ellipse 70px 170px at 95px 470px,#7e9cc4 0%,rgba(126,156,196,0) 75%),
    radial-gradient(ellipse 220px 260px at 250px 560px,#f4f5f8 0%,rgba(244,245,248,0) 80%),
    linear-gradient(180deg,#ecdccd 0%,#efe6de 45%,#eef1f5 80%,#ffffff 100%)}
.band{left:0;top:166px;width:1200px;height:37px;
  background:linear-gradient(90deg,var(--band-dark),var(--band) 40%,#3f83d4 60%,var(--band))}
.band h2{position:absolute;top:5px;font-family:"Open Sans",sans-serif;font-size:21px;color:var(--white);letter-spacing:-.4px;font-weight:700;white-space:nowrap}
.band h2 span{font-weight:300}

.brand{display:flex;align-items:center;gap:8px}
.brand-mark{border-radius:50%;border:5px solid var(--blue);background:var(--white)}
.brand-name{font-family:"Mulish",sans-serif;font-weight:700;color:var(--navy);letter-spacing:1px;line-height:1}

.copy{font-size:12.9px;line-height:18.2px;letter-spacing:.35px;white-space:nowrap}
.copy b{font-weight:700}
.gap{margin-top:18.2px}
.mission-title{font-weight:700;font-size:12.9px;line-height:18.2px;letter-spacing:.7px}
.mission-list{list-style:none;font-size:12.9px;letter-spacing:.75px;line-height:18.2px;white-space:nowrap}
.mission-list li{display:flex;align-items:center;gap:4px;margin-left:-2px}
.mission-list li::before{content:"";width:9px;height:9px;border-radius:50%;border:2px solid var(--blue);background:radial-gradient(var(--blue) 35%,transparent 42%)}

.quote{left:46px;top:722px;width:305px;height:124px;background:linear-gradient(120deg,var(--blue),#3d86dc);
  border-bottom:4px solid var(--navy);color:var(--white);padding:6px 8px 0 8px}
.quote::before{content:"";position:absolute;top:-12px;left:262px;border:12px solid transparent;border-top:0;border-bottom-color:#3a84da}
.quote p{font-family:"Open Sans",sans-serif;font-weight:300;font-size:14px;line-height:20.6px;text-transform:uppercase;letter-spacing:-.45px;white-space:nowrap}
.quote cite{display:block;font-style:normal;font-family:"Mulish",sans-serif;font-weight:700;font-size:12.6px;margin-top:2px}

.contact-name{font-weight:700;font-size:12.4px;letter-spacing:.45px;line-height:18.2px}
.contact-list{list-style:none;font-size:12.9px;line-height:18.3px;letter-spacing:.45px}
.contact-list li{display:flex;align-items:center;gap:8px}
.contact-list svg{width:16px;height:16px}

.headline{left:812px;top:656px;width:368px;height:148px;background:linear-gradient(120deg,var(--blue),#3c86dc);
  border-bottom:4px solid var(--navy);padding:9px 13px;color:var(--white)}
.headline::before{content:"";position:absolute;top:-15px;left:268px;border:16px solid transparent;border-top:0;border-bottom-color:#2f7ad5}
.headline p{font-family:"Open Sans",sans-serif;font-weight:300;font-size:29px;line-height:31.6px;letter-spacing:-1px;text-transform:uppercase;white-space:nowrap}
.headline b{font-weight:700}
</style>
</head>
<body>

<div class="abs hero-strip" role="img" aria-label="Photo of a row of smiling healthcare professionals in white coats with stethoscopes"></div>
<div class="abs sweep"></div>
<div class="abs side-photo" role="img" aria-label="Photo of a smiling female doctor with a stethoscope, a male colleague in shirt and tie behind her"></div>

<div class="abs brand" style="left:33px;top:74px">
  <div class="brand-mark" style="width:48px;height:48px"></div>
  <span class="brand-name" style="font-size:44px">BRVL</span>
</div>
<div class="abs brand" style="left:844px;top:62px">
  <div class="brand-mark" style="width:64px;height:64px;border-width:7px"></div>
  <span class="brand-name" style="font-size:58px">BRVL</span>
</div>

<div class="abs band">
  <h2 style="left:51px">ABOUT <span>US</span></h2>
  <h2 style="left:449px">APPLICATION <span>PROCESS</span></h2>
  <h2 style="left:889px;top:7px">MODERNIZE <span>HEALTHCARE</span></h2>
</div>

<section class="abs" style="left:51px;top:225px">
  <p class="copy">Here at the <b>Northfield Council of Clinical</b><br><b>Standards</b>, we believe that the <b>highest quality</b><br><b>in healthcare</b> comes from the <b>highest quality</b><br><b>people</b>. We envision a care environment that<br>is focused on quality, enabled by healthcare<br>professionals who have been well trained in<br>quality subjects and who are as passionate as<br>we are about improving the delivery of healthcare.</p>
  <h3 class="mission-title gap">OUR MISSION</h3>
  <ul class="mission-list">
    <li>QUALITY IN ALL THAT WE DO AND OFFER</li>
    <li>INTEGRITY IN ALL OF OUR WORK</li>
    <li>INNOVATIONS IN TRAINING AND EDUCATION</li>
    <li>LEADERSHIP WORLDWIDE</li>
    <li>CONTINUOUS EDUCATION</li>
  </ul>
  <p class="copy gap"><b>Our mission</b> is to enhance quality in healthcare<br>by transforming the professionals who work in<br>healthcare. We aim to give you the tools and<br>knowledge that you need to impact healthcare<br>delivery and outcomes and to be an advocate<br>for quality and patient safety.</p>
</section>

<blockquote class="abs quote">
  <p>&ldquo;Lorem ipsum dolor sit amet, consses<br>etur adipiscing elit. Nam port titored<br>aliquet massa, quis bibendum sapiens<br>dictum id vestibulum eleme.&rdquo;</p>
  <cite>Harlan Voss Company ltd.</cite>
</blockquote>

<section class="abs" style="left:452px;top:225px">
  <p class="copy">Lorem ipsum dolor sit amet, consectetur<br>adipiscing elit. Aenean sollicitudin vestibulum<br>feugiat. Quisque gravida nec purus vitae rutrum.<br>Morbi sed libero id augue pellentesque placerat<br>sed a nisl. Integer et orci ut est malesuada<br>mollis vitae adipiscing orci. Donec quis tellus in<br>lacus bibendum lobortis. Sed tempus diam<br>lacus, ut accumsan urna congue in. Aenean eget<br>suscipit purus. Maecenas dui tortor, pulvinar eu<br>felis a, facilisis eleifend nibh. Suspendisse id est<br>viverra, pellentesque lacus ac, rhoncus mauris.</p>
  <p class="copy gap">Donec pharetra risus et mauris tempus, nec<br>sodales elit rhoncus. Nam vulputate congue<br>vestibulum.</p>
  <p class="copy gap" style="font-style:italic">Feel free to contact us to discuss the course<br>that will be the right fit for you.</p>
</section>

<div class="abs brand" style="left:448px;top:692px">
  <div class="brand-mark" style="width:52px;height:52px"></div>
  <span class="brand-name" style="font-size:46px">BRVL</span>
</div>

<address class="abs" style="left:449px;top:754px;font-style:normal">
  <p class="contact-name">Northfield Council of Clinical Standards</p>
  <p class="copy">1875 Larkspur Ave.<br>Fairhaven, OK 73990</p>
  <ul class="contact-list" style="margin-top:6px">
    <li><svg viewBox="0 0 16 16"><circle cx="8" cy="8" r="7" fill="none" stroke="#1f6fd1" stroke-width="2"/><path d="M5 4.5l2 2-1 1a5 5 0 0 0 2.5 2.5l1-1 2 2-1 1.2C7.5 12 4 8.5 3.8 5.5z" fill="#0d1b6e"/></svg>(555) 014-2729</li>
    <li><svg viewBox="0 0 16 16"><circle cx="8" cy="8" r="7" fill="none" stroke="#1f6fd1" stroke-width="2"/><rect x="4.5" y="6" width="7" height="5" rx="1" fill="#0d1b6e"/><rect x="6" y="4" width="4" height="2" fill="#0d1b6e"/></svg>(555) 014-0777</li>
    <li><svg viewBox="0 0 16 16"><circle cx="8" cy="8" r="7" fill="none" stroke="#1f6fd1" stroke-width="2"/><rect x="4.5" y="5.5" width="7" height="5" fill="#0d1b6e"/><path d="M4.5 5.5L8 8.5l3.5-3" stroke="#fff" fill="none"/></svg>info@brvl-council.org</li>
    <li><svg viewBox="0 0 16 16"><circle cx="8" cy="8" r="7" fill="none" stroke="#1f6fd1" stroke-width="2"/><circle cx="8" cy="8" r="3.6" fill="#0d1b6e"/><path d="M4.4 8h7.2M8 4.4v7.2" stroke="#fff" stroke-width=".8"/></svg>www.brvl-council.org</li>
  </ul>
</address>

<div class="abs headline">
  <p>The <b>highest quality</b><br>in <b>healthcare</b> comes<br>from the <b>highest</b><br><b>quality people</b></p>
</div>

</body>
</html>
```